TRL Cards
Business Cards - Financial Services
Business Cards
Professional
Dominic Hale
Managing Director of Digital Services
387 Marlowe St Suite 204 New York, NY 10017
dhale@trlwealthco.example
www.trlwealthco.example
sarmadshaikh sarmadshaikh
sir its not getting aplosd
ruxanda ruxanda
Please uploud your logo in .ai format

```html
<!DOCTYPE html>
<html lang="en">
<head>
<meta charset="utf-8">
<title>TRL Cards – Business Cards</title>
<link href="https://fonts.googleapis.com/css2?family=Raleway:wght@500;700&family=Open+Sans:wght@400;600&display=swap" rel="stylesheet">
<style>
  :root {
    --stage: #8a8b8d;
    --green-dark: #1d5a2a;
    --green: #2e7a3b;
    --green-light: #3f9150;
    --gold: #b3873f;
    --card-white: #ffffff;
    --ink: #4a4a4a;
    --rule: #d7d7d7;
  }
  * { box-sizing: border-box; margin: 0; padding: 0; }
  html, body { width: 1200px; height: 908px; overflow: hidden; }
  body {
    background: var(--stage);
    font-family: "Open Sans", sans-serif;
    position: relative;
  }
  .card {
    position: absolute;
    width: 540px;
    height: 310px;
    border-radius: 18px;
    overflow: hidden;
    box-shadow: 0 10px 24px rgba(0,0,0,0.25);
  }
  /* Front */
  .card--front {
    left: 30px; top: 299px;
    background: linear-gradient(135deg, var(--green-light) 0%, var(--green) 45%, var(--green-dark) 100%);
  }
  .card--front .accent-disc {
    position: absolute;
    right: 40px; top: 30px;
    width: 240px; height: 240px;
    border-radius: 50%;
    background: radial-gradient(circle at 40% 35%, rgba(255,255,255,0.16), rgba(255,255,255,0.04) 70%);
  }
  .card--front .wordmark {
    position: absolute;
    left: 36px; bottom: 58px;
    color: var(--card-white);
  }
  .wordmark .name {
    font-family: "Raleway", sans-serif;
    font-weight: 700;
    font-size: 30px;
    letter-spacing: 1px;
    line-height: 1;
  }
  .wordmark .sub {
    font-family: "Raleway", sans-serif;
    font-weight: 700;
    font-size: 13px;
    letter-spacing: 2.5px;
    margin-top: 6px;
  }
  /* Back */
  .card--back {
    left: 630px; top: 299px;
    background: var(--card-white);
  }
  .tab {
    position: absolute;
    width: 120px; height: 12px;
    background: var(--green);
    border-radius: 6px;
  }
  .tab--tl { left: -20px; top: -4px; }
  .tab--tr { right: -20px; top: -4px; }
  .tab--bl { left: -20px; bottom: -4px; }
  .tab--br { right: -20px; bottom: -4px; }
  .brand {
    position: absolute;
    left: 34px; top: 70px;
    display: flex; align-items: center; gap: 12px;
  }
  .brand .dot {
    width: 44px; height: 44px; border-radius: 50%;
    background: var(--green);
  }
  .brand .name {
    font-family: "Raleway", sans-serif;
    font-weight: 700;
    font-size: 24px;
    color: var(--green);
    line-height: 1;
  }
  .brand .sub {
    font-family: "Raleway", sans-serif;
    font-weight: 700;
    font-size: 10px;
    letter-spacing: 1.6px;
    color: var(--green);
    margin-top: 5px;
  }
  .person {
    position: absolute;
    left: 34px; top: 190px;
  }
  .person .person-name {
    font-weight: 600;
    font-size: 17px;
    color: var(--green);
  }
  .person .person-title {
    font-size: 11.5px;
    color: var(--gold);
    margin-top: 3px;
  }
  .divider {
    position: absolute;
    left: 312px; top: 60px;
    width: 1px; height: 190px;
    background: var(--rule);
  }
  .contact {
    position: absolute;
    left: 330px; top: 62px;
    list-style: none;
    font-size: 11px;
    color: var(--ink);
  }
  .contact .address { line-height: 1.5; margin-bottom: 10px; }
  .contact li.line { display: flex; align-items: center; gap: 8px; margin-bottom: 7px; }
  .icon {
    width: 16px; height: 16px; flex: none;
  }
</style>
</head>
<body>
  <section class="card card--front" aria-label="Card front">
    <div class="accent-disc"></div>
    <div class="wordmark">
      <div class="name">TRL WEALTH</div>
      <div class="sub">COMPANY, LLC</div>
    </div>
  </section>

  <section class="card card--back" aria-label="Card back">
    <span class="tab tab--tl"></span>
    <span class="tab tab--tr"></span>
    <span class="tab tab--bl"></span>
    <span class="tab tab--br"></span>

    <div class="brand">
      <span class="dot"></span>
      <div>
        <div class="name">TRL WEALTH</div>
        <div class="sub">COMPANY, LLC</div>
      </div>
    </div>

    <div class="person">
      <div class="person-name">Dominic Hale</div>
      <div class="person-title">Managing Director of Digital Services</div>
    </div>

    <div class="divider"></div>

    <ul class="contact">
      <li class="address">387 Marlowe St<br>Suite 204<br>New York, NY 10017</li>
      <li class="line">
        <svg class="icon" viewBox="0 0 16 16"><circle cx="8" cy="8" r="8" fill="#2e7a3b"/><path d="M5.2 4.5l1.4-.3.8 1.8-.9.7c.4.9 1 1.5 1.9 1.9l.7-.9 1.8.8-.3 1.4c-3 .2-5.6-2.4-5.4-5.4z" fill="#fff"/></svg>
        <span>212-555-0148</span>
      </li>
      <li class="line">
        <svg class="icon" viewBox="0 0 16 16"><circle cx="8" cy="8" r="8" fill="#2e7a3b"/><rect x="5.5" y="3.8" width="5" height="8.4" rx="1" fill="none" stroke="#fff" stroke-width="1"/><circle cx="8" cy="10.8" r=".6" fill="#fff"/></svg>
        <span>212-555-0193</span>
      </li>
      <li class="line">
        <svg class="icon" viewBox="0 0 16 16"><circle cx="8" cy="8" r="8" fill="#2e7a3b"/><rect x="4" y="5" width="8" height="6" fill="none" stroke="#fff" stroke-width="1"/><path d="M4 5l4 3.2L12 5" fill="none" stroke="#fff" stroke-width="1"/></svg>
        <span>dhale@trlwealthco.example</span>
      </li>
      <li class="line">
        <svg class="icon" viewBox="0 0 16 16"><circle cx="8" cy="8" r="8" fill="#2e7a3b"/><circle cx="8" cy="8" r="4" fill="none" stroke="#fff" stroke-width="1"/><path d="M4 8h8M8 4c-2 2.4-2 5.6 0 8M8 4c2 2.4 2 5.6 0 8" fill="none" stroke="#fff" stroke-width=".8"/></svg>
        <span>www.trlwealthco.example</span>
      </li>
    </ul>
  </section>
</body>
</html>
```